New product brand / design for paints "Tovrel"

We are looking for a label design for various paint products. The brand name should be Tovrel and have a Scandinavian-Nordic appearance. The following key points should be considered: down-to-earth and rustic, environmentally friendly, Nordic, coastal and sea.
The following link serves as an example: https://pinselwerk-demo.com/search?q=mirelo*&type=product.
The same design is intended to serve multiple paint products and be used on cans.

```html
<!DOCTYPE html>
<html lang="de">
<head>
<meta charset="utf-8">
<title>Tovrel Holzlasur – Etikett</title>
<link rel="stylesheet" href="https://fonts.googleapis.com/css2?family=Montserrat:wght@700;800&display=swap">
<style>
  :root {
    --backdrop: #e4e4e4;
    --navy-deep: #06124a;
    --navy-mid: #0b1e63;
    --navy-edge: #13297a;
    --sea-blue: #1c5aa8;
    --sea-light: #2f73c0;
    --copper: #c08a5e;
    --copper-light: #d3a27a;
    --white: #f4f4f4;
  }
  * { margin: 0; padding: 0; box-sizing: border-box; }
  html, body {
    width: 1200px;
    height: 800px;
    overflow: hidden;
    background: var(--backdrop);
  }
  .canvas {
    position: relative;
    width: 1200px;
    height: 800px;
  }
  .label {
    position: absolute;
    left: 240px;
    top: 17px;
    width: 720px;
    height: 766px;
    overflow: hidden;
    background: linear-gradient(90deg, var(--navy-edge) 0%, var(--navy-deep) 18%, var(--navy-mid) 50%, var(--navy-deep) 82%, var(--navy-edge) 100%);
  }
  .ship-art {
    position: absolute;
    left: 30px;
    top: 80px;
    width: 660px;
    height: 320px;
    background: radial-gradient(ellipse at 50% 55%, rgba(28, 90, 168, 0.55) 0%, rgba(28, 90, 168, 0.25) 45%, rgba(28, 90, 168, 0) 72%);
  }
  .brand-mark {
    position: absolute;
    left: 50%;
    top: 95px;
    width: 200px;
    height: 200px;
    margin-left: -100px;
    border: 10px solid var(--copper);
    border-radius: 50%;
  }
  .brand-name {
    position: absolute;
    left: 0;
    right: 0;
    top: 316px;
    text-align: center;
    font-family: "Montserrat", sans-serif;
    font-weight: 700;
    font-size: 66px;
    letter-spacing: 8px;
    color: var(--copper);
    text-transform: uppercase;
  }
  .product-name {
    position: absolute;
    left: 0;
    right: 0;
    top: 454px;
    text-align: center;
    font-family: "Montserrat", sans-serif;
    font-weight: 800;
    font-size: 82px;
    letter-spacing: 1px;
    color: var(--white);
  }
  .coverage-tag {
    position: absolute;
    left: 393px;
    top: 562px;
    width: 246px;
    height: 46px;
    background: var(--copper);
    transform: rotate(-2deg);
    font-family: "Montserrat", sans-serif;
    font-weight: 700;
    font-size: 22px;
    line-height: 46px;
    text-align: center;
    color: var(--white);
    z-index: 2;
  }
  .wave-band {
    position: absolute;
    left: 0;
    right: 0;
    top: 600px;
    height: 102px;
    background: linear-gradient(180deg, rgba(28, 90, 168, 0.35) 0%, var(--sea-blue) 45%, var(--sea-light) 100%);
  }
  .copper-band {
    position: absolute;
    left: 0;
    right: 0;
    top: 702px;
    height: 64px;
    background: linear-gradient(180deg, var(--copper) 0%, var(--copper-light) 50%, var(--copper) 100%);
  }
</style>
</head>
<body>
<main class="canvas">
  <section class="label">
    <div class="ship-art" role="img" aria-label="Illustration zweier Wikingerschiffe in Blau, die das Markenzeichen flankieren"></div>
    <div class="brand-mark"></div>
    <h1 class="brand-name">Tovrel</h1>
    <h2 class="product-name">HOLZLASUR</h2>
    <p class="coverage-tag">10-12m² pro Liter</p>
    <div class="wave-band" role="img" aria-label="Dekoratives Wellenmuster in Meeresblau"></div>
    <div class="copper-band"></div>
  </section>
</main>
</body>
</html>
```